Velmorra Design Group Business Card Design

We need a double-sided business card for our company Velmorra Design Group. Our slogan is "Simple Online Solutions." We are looking for a techy, cutting-edge but simple card that looks modern and sleek. We have a black logo attached and would prefer a lighter background to make our logo stand out. We like nice accents to make it pop out and make our clients remember our card.

On the back side, we just want our logo, slogan and website. Again, something very simple. Make the logo big on the back.

```html
<!DOCTYPE html>
<html lang="en">
<head>
<meta charset="utf-8">
<title>Velmorra Design Group — Business Card</title>
<link rel="stylesheet" href="https://fonts.googleapis.com/css2?family=Arimo:wght@400&family=Pinyon+Script&display=swap">
<style>
  :root {
    --card-bg: #efeeef;
    --ink: #111111;
    --logo-ink: #1c1c1c;
    --crop-mark: #111111;
    --light-text: #ffffff;
    --soft-shadow: rgba(0, 0, 0, 0.55);
  }
  html, body {
    margin: 0;
    padding: 0;
    width: 1200px;
    height: 751px;
    overflow: hidden;
    background: var(--card-bg);
  }
  .card {
    position: relative;
    width: 1200px;
    height: 751px;
    background: var(--card-bg);
    font-family: "Arimo", Arial, sans-serif;
  }
  .crop-marks {
    position: absolute;
    inset: 0;
  }
  .brand-name {
    position: absolute;
    top: 160px;
    left: 0;
    width: 100%;
    margin: 0;
    text-align: center;
    font-family: "Arimo", Arial, sans-serif;
    font-weight: 400;
    font-size: 66px;
    letter-spacing: 1px;
    color: var(--logo-ink);
  }
  .slogan {
    position: absolute;
    top: 306px;
    left: 0;
    width: 100%;
    margin: 0;
    text-align: center;
    font-family: "Pinyon Script", cursive;
    font-size: 40px;
    color: var(--light-text);
    text-shadow: 1px 2px 3px var(--soft-shadow), 0 0 1px rgba(0,0,0,0.6);
  }
  .phone-numbers {
    position: absolute;
    top: 436px;
    left: 0;
    width: 100%;
    margin: 0;
    text-align: center;
    font-size: 44px;
    color: var(--ink);
    text-shadow: 3px 4px 6px rgba(0, 0, 0, 0.35);
  }
  .services {
    position: absolute;
    top: 528px;
    left: 0;
    width: 100%;
    margin: 0;
    text-align: center;
    font-size: 27px;
    line-height: 35px;
    color: var(--light-text);
    text-shadow: 2px 3px 5px var(--soft-shadow);
  }
</style>
</head>
<body>
<main class="card">
  <svg class="crop-marks" width="1200" height="751" viewBox="0 0 1200 751" aria-hidden="true">
    <g stroke="var(--crop-mark)" stroke-width="3" fill="none">
      <line x1="72" y1="0" x2="72" y2="60"/>
      <line x1="0" y1="80" x2="59" y2="80"/>
      <line x1="1132" y1="0" x2="1132" y2="56"/>
      <line x1="1148" y1="80" x2="1200" y2="80"/>
      <line x1="0" y1="686" x2="50" y2="686"/>
      <line x1="72" y1="708" x2="72" y2="751"/>
      <line x1="1132" y1="708" x2="1132" y2="751"/>
      <line x1="1158" y1="686" x2="1200" y2="686"/>
    </g>
  </svg>

  <h1 class="brand-name">Velmorra Design Group</h1>
  <p class="slogan">Simple Online Solutions</p>
  <p class="phone-numbers">647-555-0142 | 647-555-0187</p>
  <p class="services">Website Design, Social Media Marketing, Logo Design,<br>Search Engine Optimization, Web Video Production</p>
</main>
</body>
</html>
```